Guaranteed Job - Sleek Sexy Business Card UV Spot

Im looking for a sleek and sexy business card, that resembles elite or VIP status status.
our business is corinvale.example
you can view our products on there, but our main audience for handing out our cards will be for people in the hospitality industry, so it will need to impress high management and CEO of hotels and restaurants, bars, clubs etc...
the card features will have UV spot on both sides, 400gsm stock. standard size.
Artwork should be 86 x 54mm + 2mm bleed = 90 x 58mm
it should have a nice "unique" uv spot pattern that highlights the card, not a repeated pattern, theres no originality there, and it will be disregarded.
The written material will be:
Corin Vale Hospitality College (logo)
Tobin Marsh
Director
Phone: 1300 615 737
Mobile: 0455 817 296
Email: info@corinvale.example
website: www.corinvale.example
I'm looking for originality here, i don't want just a simple stock card, want something that has a wow factor for people.
You will find the logo attached. you may invert the white to black words to suit the background as you please.
thank you and good luck
As a side note, ive received a lot of proposals, im too busy to give feedback to each and every one, so if i havent provided feedback for your design within 24 hours, then consider it not acceptable, and you could resubmit another design.
So far i have not seen any design that stood out for me, they all seem pretty generic. there nothing thats unique, i would figure for the amount that im offering, that people would put some more effort and creativity into the design.
so far over 200 designs submitted, and nothing i have seen looks very original, everything looks like a different variation of the same stuff, i said it very clearly i wanted something unique, the only thing that has come close to it so far is this one
Reason: Ive received alot of design concepts and i have reviewed everyone, but i havent had time to give feedback to every single one, only the ones that have interested me, if i havent responded, its because i havent found it good enough.
so far only a few design have been on par with what ive been looking for, an attractive eye popping design.
heres a few of them,
http://files.pixelbazaar.example/design_img/51736/62418/62418_2840915_51736_image.jpg
http://files.pixelbazaar.example/design_img/51736/68254/68254_2841377_51736_image.jpg
theyre, both unique and original, and eye catching, the only thing theyre missing is the sexyness.
if you still think you have some creativity left in your minds, then throw it on here.
Reason: Sorry guys for the delay, I was in a serious accident and out of commission for the past few months, I'm just slowly recovering now, please bare with me as i try to attend to this project, it may take me awhile as I have other projects that are on standby, I'm not 100% at the moment, so im extending the deadline for 2 weeks right now. Thanks for your patience.
Hospitality

```html
<!DOCTYPE html>
<html lang="en">
<head>
<meta charset="utf-8">
<title>Corin Vale Hospitality College — Business Card</title>
<link rel="stylesheet" href="https://fonts.googleapis.com/css2?family=Barlow:wght@500&family=Archivo+Black&display=swap">
<style>
  :root {
    --frame: #454d4f;
    --card-black: #0b0c0d;
    --card-charcoal: #2a2d30;
    --band-deep: #0a1a6e;
    --band-bright: #2f6dff;
    --band-glow: #8fb6ff;
    --ice: #6ccff6;
    --white: #ffffff;
    --ink: #0a0a0a;
  }
  * { margin: 0; padding: 0; box-sizing: border-box; }
  html, body {
    width: 1200px;
    height: 773px;
    overflow: hidden;
    background: var(--frame);
  }
  .card {
    position: relative;
    width: 1200px;
    height: 773px;
    background: var(--frame);
  }
  .card-face {
    position: absolute;
    left: 27px;
    top: 27px;
    width: 1147px;
    height: 720px;
    overflow: hidden;
    background:
      radial-gradient(ellipse at 45% 40%, var(--card-charcoal) 0%, var(--card-black) 70%);
  }
  .brushed-band {
    position: absolute;
    left: 0;
    width: 100%;
    height: 73px;
    background:
      linear-gradient(90deg, var(--band-deep) 0%, var(--band-bright) 22%, var(--band-glow) 50%, var(--band-bright) 78%, var(--band-deep) 100%);
  }
  .brushed-band--top { top: 0; }
  .brushed-band--bottom { bottom: 0; }
  .brand-mark {
    position: absolute;
    left: 190px;
    top: 258px;
    width: 240px;
    height: 240px;
    background: var(--ice);
  }
  .brand-name {
    position: absolute;
    left: 498px;
    top: 268px;
    font-family: 'Barlow', sans-serif;
    font-weight: 500;
    color: var(--white);
    text-transform: uppercase;
    line-height: 1;
  }
  .brand-name__line {
    display: block;
  }
  .brand-name__line--primary {
    font-size: 114px;
    letter-spacing: 2px;
    margin-bottom: 12px;
  }
  .brand-name__line--secondary {
    font-size: 44px;
    letter-spacing: 3px;
  }
  .website {
    position: absolute;
    left: 0;
    width: 1147px;
    bottom: 12px;
    text-align: center;
    font-family: 'Archivo Black', sans-serif;
    font-size: 40px;
    letter-spacing: 9px;
    color: var(--ink);
    -webkit-text-stroke: 1.5px var(--white);
    text-shadow: 0 0 2px var(--white), 0 0 3px var(--white);
    line-height: 1;
  }
</style>
</head>
<body>
  <div class="card">
    <div class="card-face" role="img" aria-label="Black brushed-metal card background">
      <div class="brushed-band brushed-band--top" role="img" aria-label="Blue brushed-metal streak band"></div>

      <div class="brand-mark"></div>
      <div class="brand-name">
        <span class="brand-name__line brand-name__line--primary">Corin Vale</span>
        <span class="brand-name__line brand-name__line--secondary">Hospitality College</span>
      </div>

      <div class="brushed-band brushed-band--bottom" role="img" aria-label="Blue brushed-metal streak band"></div>
      <p class="website">www.corinvale.example</p>
    </div>
  </div>
</body>
</html>
```